Bourbon label design for bourbon brand. Looking to freshen our current label.

I need a Bourbon label design for our rebranded Bourbon bottle. Label should include picture of our horse and our logo on the bottle. Front Label is 3.5 inches wide and 6 inches tall, back label is 4 inches tall and 3 inches wide. Back label can be a simple plain logo like the one in the brief. I have included a design of our current bottle and label. We want to stay close to the current color schemes but want a fresh rebrand of the design. The label needs to be the correct size on a tall bottle like pictured.

Target Market(s)

Our Bourbon members, 30-50 year old males

Requirements
Must have
• Picture of our horse, our B logo , straight Bourbon whiskey on the front. Room to edit text on the back label.

```html
<!DOCTYPE html>
<html lang="en">
<head>
<meta charset="utf-8">
<title>Nightfall Straight Bourbon Whiskey – Labels</title>
<link href="https://fonts.googleapis.com/css2?family=Oswald:wght@500;700&family=Lato:wght@400&display=swap" rel="stylesheet">
<style>
  :root {
    --board: #dcdcdc;
    --ink: #000000;
    --paper: #ffffff;
    --silver-dark: #9f9f9f;
    --silver: #b9b9b9;
    --silver-light: #d6d6d6;
    --body-grey: #cfcfcf;
  }
  * { margin: 0; padding: 0; box-sizing: border-box; }
  html, body { width: 1000px; height: 1200px; overflow: hidden; }
  body {
    background: var(--board);
    position: relative;
    font-family: "Oswald", "Arial Narrow", sans-serif;
  }

  /* Front label 3.5 x 6 in */
  .front-label {
    position: absolute; left: 70px; top: 240px;
    width: 420px; height: 720px;
    background: linear-gradient(to bottom, var(--silver-dark) 0%, #c8c8c8 45%, var(--paper) 75%, var(--paper) 100%);
    overflow: hidden;
  }
  .front-label .panel-shape { position: absolute; inset: 0; }
  .front-label .product-name {
    position: absolute; left: 30px; top: 62px; width: 370px;
    font-weight: 700; font-size: 82px; line-height: 1;
    letter-spacing: -1px; text-align: center;
    color: var(--silver-light);
    transform: scaleY(1.08);
  }
  .front-label .style-band { position: absolute; left: 0; top: 151px; width: 420px; height: 36px; }
  .front-label .style-name {
    position: absolute; left: 60px; top: 152px; width: 305px;
    font-weight: 700; font-size: 24px; line-height: 34px;
    text-align: center; color: var(--ink);
  }
  .front-label .barrel-notes {
    position: absolute; right: 36px; top: 214px;
    text-align: right; color: var(--silver);
    font-weight: 500; font-size: 16px; line-height: 21px; letter-spacing: .5px;
  }
  .barrel-notes .rule { display: block; width: 16px; height: 2px; background: var(--silver); margin: 8px 0 10px auto; }
  .front-label .horse-photo {
    position: absolute; left: 93px; top: 204px; width: 162px; height: 430px;
    background: radial-gradient(ellipse at 50% 45%, #7d7d7d 0%, #9a9a9a 45%, rgba(200,200,200,0) 75%);
  }
  .front-label .brand-mark {
    position: absolute; left: 278px; top: 566px; width: 126px;
    display: flex; flex-direction: column; align-items: center; gap: 8px;
  }
  .brand-mark .dot { width: 46px; height: 46px; border-radius: 50%; background: var(--paper); }
  .front-label .brand-mark .name { color: var(--paper); font-weight: 700; font-size: 18px; letter-spacing: 1px; }
  .front-label .fill-rule {
    position: absolute; left: 31px; top: 652px; width: 204px; height: 4px; background: var(--ink);
  }
  .front-label .fill-fields {
    position: absolute; left: 31px; top: 664px; width: 225px;
    display: flex; justify-content: space-between;
    font-weight: 700; font-size: 12px; color: var(--ink);
  }

  /* Back label 3 x 4 in */
  .back-label {
    position: absolute; left: 545px; top: 410px;
    width: 390px; height: 520px;
    background: var(--ink); overflow: hidden;
  }
  .back-label .panel-shape { position: absolute; inset: 0; }
  .back-label .product-name {
    position: absolute; right: 30px; top: 62px;
    font-weight: 700; font-size: 52px; line-height: 1;
    color: var(--silver-dark); letter-spacing: -1px;
  }
  .back-label .style-name {
    position: absolute; right: 30px; top: 124px;
    font-weight: 700; font-size: 17px; color: var(--silver-light);
  }
  .back-label .rule { position: absolute; right: 30px; top: 157px; width: 18px; height: 2px; background: var(--paper); }
  .back-label .story {
    position: absolute; right: 30px; top: 173px; width: 270px;
    font-family: "Lato", "Helvetica", sans-serif;
    font-size: 13.5px; line-height: 18.2px; text-align: right; color: var(--body-grey);
  }
  .back-label .brand-mark {
    position: absolute; left: 18px; top: 436px; width: 76px;
    display: flex; flex-direction: column; align-items: center; gap: 4px;
  }
  .back-label .brand-mark .dot { width: 28px; height: 28px; border-radius: 0; background: var(--ink); }
  .back-label .brand-mark .name { color: var(--ink); font-weight: 700; font-size: 13px; line-height: 16px; letter-spacing: .5px; }
</style>
</head>
<body>

<section class="front-label" aria-label="Front label">
  <svg class="panel-shape" viewBox="0 0 420 720" aria-hidden="true">
    <path d="M170 0 H420 V720 H330 A75 75 0 0 1 255 645 V95 C255 40 232 0 170 0 Z" fill="var(--ink)"/>
  </svg>
  <h1 class="product-name">NIGHTFALL</h1>
  <svg class="style-band" viewBox="0 0 420 36" aria-hidden="true">
    <polygon points="255,0 385,0 365,36 255,36" fill="var(--silver-dark)"/>
  </svg>
  <p class="style-name">STRAIGHT BOURBON WHISKEY</p>
  <div class="barrel-notes">
    SINGLE<br>BARREL
    <span class="rule"></span>
    BARREL<br>STRENGTH
    <span class="rule"></span>
  </div>
  <div class="horse-photo" role="img" aria-label="Black and white photograph of the racehorse with jockey galloping toward the viewer"></div>
  <div class="brand-mark">
    <span class="dot"></span>
    <span class="name">NIGHTFALL</span>
  </div>
  <div class="fill-rule"></div>
  <div class="fill-fields">
    <span>BARREL NO.</span><span>AGED/YEARS</span><span>ALC./VOL.</span>
  </div>
</section>

<section class="back-label" aria-label="Back label">
  <svg class="panel-shape" viewBox="0 0 390 520" aria-hidden="true">
    <defs>
      <linearGradient id="back-fade" x1="0" y1="0" x2="0" y2="1">
        <stop offset="0" stop-color="#000000"/>
        <stop offset="0.45" stop-color="#9a9a9a"/>
        <stop offset="1" stop-color="#ffffff"/>
      </linearGradient>
    </defs>
    <path d="M0 150 C0 420 120 520 360 520 H0 Z" fill="url(#back-fade)"/>
  </svg>
  <h2 class="product-name">NIGHTFALL</h2>
  <p class="style-name">STRAIGHT BOURBON WHISKEY</p>
  <span class="rule"></span>
  <p class="story">Lorem ipsum dolor sit amet, consectetur adipiscing elit. Quisque placerat sem at nunc venenatis venenatis. Vestibulum dapibus dui lectus, non accumsan mauris tincidunt et. In non viverra turpis. Aenean id finibus magna, et feugiat ipsum. Proin laoreet gravida lorem nec porta. Suspendisse a neque dictum, tempus lorem ac, suscipit dolor. Fusce id eleifend dolor. Quisque rhoncus sem vel tortor dapibus accumsan.</p>
  <div class="brand-mark">
    <span class="dot"></span>
    <span class="name">NIGHTFALL</span>
  </div>
</section>

</body>
</html>
```